Income Tax Business Cards - Updates

Need to update these business cards while keeping all the same wording but just update them and make them look nicer and more modern/ on brand with our brand.

Industry/Entity Type

finance

Contact Information for Business Card

we have multiple locations so will just need to easily be able to change the address and phone numbers

Colors

Designer to choose colors to be used in the design.

```html
<!DOCTYPE html>
<html lang="en">
<head>
<meta charset="utf-8">
<title>Ledgerline Financial Group – Business Cards</title>
<link rel="stylesheet" href="https://fonts.googleapis.com/css2?family=Cinzel:wght@400;600&family=Montserrat:wght@700;800&family=Open+Sans:wght@400;600&display=swap">
<style>
  :root {
    --green: #0f5a30;
    --green-deep: #0b4826;
    --red: #c4202a;
    --white: #ffffff;
    --ink: #1f2a24;
    --backdrop: #2a2c2e;
  }
  * { box-sizing: border-box; margin: 0; padding: 0; }
  html, body { width: 1200px; height: 900px; overflow: hidden; }
  body { background: var(--backdrop); position: relative; font-family: "Open Sans", sans-serif; }

  .card { position: absolute; border-radius: 18px; overflow: hidden; box-shadow: 0 14px 30px rgba(0,0,0,.45); }

  /* Front card */
  .card-front {
    left: 50px; top: 270px; width: 620px; height: 354px;
    background: linear-gradient(135deg, var(--green) 0%, var(--green-deep) 100%);
    color: var(--white); text-align: center;
  }
  .brand { position: absolute; left: 0; right: 0; top: 82px; }
  .brand-name { font-family: "Cinzel", serif; font-weight: 400; font-size: 56px; letter-spacing: 2px; line-height: 1; }
  .brand-sub { font-family: "Cinzel", serif; font-weight: 400; font-size: 17px; letter-spacing: 9px; margin-top: 12px; }
  .front-offer { position: absolute; left: 0; right: 0; top: 236px; font-family: "Montserrat", sans-serif; font-weight: 800; }
  .front-offer .headline { font-size: 30px; letter-spacing: 1px; }
  .front-offer .subline { font-size: 18px; margin-top: 6px; letter-spacing: .5px; }

  /* Back card */
  .card-back { left: 760px; top: 118px; width: 380px; height: 665px; background: var(--white); }
  .contact { position: absolute; left: 34px; top: 40px; }
  .person-name { font-family: "Cinzel", serif; font-weight: 600; font-size: 30px; color: var(--green); letter-spacing: 1px; }
  .person-role { font-size: 20px; color: var(--red); margin-top: 2px; }
  .divider { width: 36px; height: 2px; background: var(--green); margin: 18px 0 16px; }
  .address { font-size: 15px; color: var(--ink); line-height: 1.45; }
  .phone { font-size: 19px; font-weight: 600; color: var(--ink); margin-top: 4px; }
  .web { font-size: 15px; color: var(--ink); margin-top: 2px; }

  .back-brand { position: absolute; left: 0; right: 0; top: 300px; text-align: center; font-family: "Cinzel", serif; font-weight: 400; font-size: 44px; color: var(--green); letter-spacing: 2px; }

  .offer-band { position: absolute; inset: 0; }
  .back-offer { position: absolute; right: 24px; top: 492px; text-align: right; color: var(--white); font-family: "Montserrat", sans-serif; font-weight: 800; line-height: 1.05; }
  .back-offer .amount { font-size: 34px; }
  .back-offer .advance { font-size: 26px; }
  .back-offer .terms { font-size: 11px; font-weight: 700; margin: 6px 0 5px; letter-spacing: .3px; }
  .back-offer .estimates { font-size: 31px; }
</style>
</head>
<body>

<section class="card card-front" aria-label="Card front">
  <div class="brand">
    <div class="brand-name">Ledgerline</div>
    <div class="brand-sub">FINANCIAL GROUP</div>
  </div>
  <div class="front-offer">
    <div class="headline">FILE YOUR TAXES HERE</div>
    <div class="subline">UP TO $6,000 SAME DAY ADVANCE</div>
  </div>
</section>

<section class="card card-back" aria-label="Card back">
  <svg class="offer-band" width="380" height="665" viewBox="0 0 380 665" aria-hidden="true">
    <path d="M0 575 Q150 420 380 392" fill="none" stroke="var(--red)" stroke-width="9"/>
    <path d="M0 594 Q160 440 380 412 L380 665 L0 665 Z" fill="var(--green)"/>
  </svg>

  <div class="contact">
    <div class="person-name">DANIEL BROOKS</div>
    <div class="person-role">Founder &amp; CEO</div>
    <div class="divider"></div>
    <div class="address">Your Address, City<br>State, Country, Zip 1235</div>
    <div class="phone">(123) 456-7890</div>
    <div class="web">www.ledgerlinefinancial.com</div>
  </div>

  <div class="back-brand">Ledgerline</div>

  <div class="back-offer">
    <div class="amount">UP TO $6,000</div>
    <div class="advance">SAME DAY ADVANCE</div>
    <div class="terms">— ON APPROVED TAX RETURNS! —</div>
    <div class="estimates">FREE ESTIMATES!</div>
  </div>
</section>

</body>
</html>
```